I need a website, primarily a landing page, for my company, Harlow Ridge. A sales training and cons

I need a web design/landing page for a new sales training and consulting company, harlow ridge. We perform "sales experiments" aimed at each individual or team, where we assist in helping them identify their strengths, through a series of "sales experiments" that we can tailor based on the individual and what they're trying to accomplish.

```html
<!DOCTYPE html>
<html lang="en">
<head>
<meta charset="utf-8">
<title>Harlow Ridge – Sales Training &amp; Consulting</title>
<link href="https://fonts.googleapis.com/css2?family=Lato:wght@400;700;900&display=swap" rel="stylesheet">
<style>
:root{
  --blue:#1f58a0;
  --blue-dark:#194b8a;
  --ink:#2f2f2f;
  --text:#555;
  --muted:#777;
  --light:#efefef;
  --topbar:#7a7a7a;
  --footer:#333;
  --footer-text:#aaa;
  --white:#fff;
}
*{box-sizing:border-box;margin:0;padding:0}
html,body{width:1200px;height:3120px;overflow:hidden}
body{font-family:'Lato',sans-serif;color:var(--text);background:var(--white);position:relative}
.abs{position:absolute}
/* header */
.topbar{left:660px;top:0;width:540px;height:52px;background:var(--topbar);clip-path:polygon(0 0,100% 0,100% 100%,24px 100%);color:var(--white);font-size:17px;display:flex;align-items:center;gap:44px;padding-left:60px}
.topbar span{display:flex;align-items:center;gap:14px}
.brand{left:74px;top:30px;display:flex;align-items:center;gap:10px;color:var(--blue);font-weight:900;font-size:20px;letter-spacing:.5px;text-transform:uppercase}
.brand i{width:26px;height:26px;border-radius:50%;background:var(--blue);display:block}
.nav{right:52px;top:82px;display:flex;gap:36px;font-size:15px;font-weight:700;color:var(--ink);text-transform:uppercase}
.nav .active{color:var(--blue)}
/* hero */
.hero{left:0;top:121px;width:1200px;height:541px;
  background:
    linear-gradient(180deg,rgba(0,0,0,.08) 0%,rgba(0,0,0,0) 40%,rgba(0,0,0,.25) 100%),
    linear-gradient(100deg,#dfe3e8 0%,#c7ccd3 18%,#b79f8c 34%,#e9e6e2 48%,#9aa3ae 62%,#5d5550 78%,#2b2a2d 100%)}
.hero h1{position:absolute;top:186px;width:100%;text-align:center;color:var(--white);font-size:52px;font-weight:900;letter-spacing:1px;text-shadow:0 2px 6px rgba(0,0,0,.35)}
.hero p{position:absolute;top:252px;width:100%;text-align:center;color:var(--white);font-size:22px;letter-spacing:1px;text-shadow:0 1px 4px rgba(0,0,0,.35)}
.dots{position:absolute;top:492px;left:566px;display:flex;gap:8px}
.dots b{width:12px;height:12px;border-radius:50%;background:var(--white);display:block}
.dots b:first-child{background:var(--blue)}
/* welcome */
.section-title{width:1200px;text-align:center;font-size:28px;font-weight:700;color:var(--ink);letter-spacing:.5px}
.welcome p{left:80px;top:776px;width:1040px;text-align:center;font-size:14px;line-height:25.5px}
.btn{display:inline-block;background:var(--blue);color:var(--white);font-weight:900;font-size:15px;text-transform:uppercase;border-radius:24px;width:186px;height:48px;line-height:48px;text-align:center}
/* feature rows */
.photo-training{background:linear-gradient(120deg,#8a8f97 0%,#eef0f2 22%,#f7f7f7 45%,#b9c1cc 62%,#d8cdbf 78%,#3b5f9a 100%)}
.photo-consult{background:linear-gradient(115deg,#eef1f4 0%,#d7dbe0 25%,#c8a892 42%,#e5e6e8 55%,#2b2f38 75%,#5a6270 100%)}
.panel{background:var(--light)}
.feature h2{font-size:28px;font-weight:700;color:var(--ink);letter-spacing:.5px;margin:16px 0 18px}
.feature p{font-size:14px;line-height:26px;width:468px;margin-bottom:26px}
/* team */
.team{left:0;top:1843px;width:1200px;height:487px;background:var(--light)}
.member{width:270px;text-align:center}
.avatar{width:158px;height:158px;border-radius:50%;margin:0 auto;border:3px solid #444;
  background:linear-gradient(180deg,#f2f2f2 0%,#d9d9d9 30%,#c9ab95 50%,#2d2f35 72%,#1d1f24 100%)}
.member h3{color:var(--blue);font-size:17px;font-weight:900;margin-top:24px}
.member .role{font-size:13px;color:var(--ink);margin-top:6px}
.member p{font-size:13px;line-height:23px;color:var(--ink);margin-top:6px}
.social{display:flex;justify-content:center;gap:20px;margin-top:18px}
.social i{width:12px;height:12px;border-radius:50%;background:#555;display:block}
/* news */
.card{top:2446px;width:329px;height:379px;border:1px solid #d6d6d6;border-radius:4px;overflow:hidden;text-align:center;box-shadow:0 1px 3px rgba(0,0,0,.08)}
.card .photo{height:190px}
.news1{background:linear-gradient(120deg,#c8ccd2 0%,#f1f2f3 30%,#6f85a8 55%,#e8e2da 75%,#3c4049 100%)}
.news2{background:linear-gradient(120deg,#f3f4f5 0%,#d3d7dc 35%,#c9a993 55%,#2f333b 80%,#e6e8ea 100%)}
.news3{background:linear-gradient(120deg,#2c3240 0%,#7f8ea5 30%,#d0b39c 50%,#f2f3f4 70%,#394152 100%)}
.card h3{color:var(--blue);font-size:19px;font-weight:700;margin-top:20px}
.card p{font-size:13.5px;line-height:23px;color:var(--ink);padding:0 26px;margin-top:6px}
.card time{display:block;color:var(--blue);font-weight:700;font-size:14px;margin-top:16px}
/* footer */
.footer{left:0;top:2887px;width:1200px;height:233px;background:var(--footer);color:var(--footer-text);font-size:13.5px}
.footer h4{color:var(--white);font-size:14px;font-weight:900;text-transform:uppercase;margin-bottom:16px}
.footer ul{list-style:none;line-height:30px}
.footer .fsocial{display:flex;gap:16px;margin-top:20px}
.footer .fsocial i{width:16px;height:16px;border-radius:50%;background:var(--footer-text);display:block}
.contact li{display:flex;gap:18px;align-items:flex-start;line-height:22px;margin-bottom:8px}
.email-input{width:240px;height:36px;border-radius:18px;background:var(--white);color:var(--ink);font-size:13px;line-height:36px;padding-left:16px}
.signup{margin:12px 0 0 150px;width:90px;height:34px;line-height:34px;border-radius:17px;background:var(--blue);color:var(--white);font-size:12px;font-weight:900;text-align:center}
</style>
</head>
<body>

<header>
  <div class="abs topbar">
    <span><svg width="16" height="16" viewBox="0 0 24 24"><path fill="#fff" d="M6.6 10.8a15 15 0 006.6 6.6l2.2-2.2c.3-.3.7-.4 1-.2 1.1.4 2.3.6 3.6.6.6 0 1 .4 1 1V20c0 .6-.4 1-1 1A17 17 0 013 4c0-.6.4-1 1-1h3.5c.6 0 1 .4 1 1 0 1.3.2 2.5.6 3.6.1.3 0 .7-.2 1z"/></svg>1-800-555-0142</span>
    <span><svg width="17" height="13" viewBox="0 0 24 18"><path fill="#fff" d="M0 0h24v2L12 10 0 2zM0 4l12 8 12-8v14H0z"/></svg>hello@harlowridge.example</span>
  </div>
  <div class="abs brand"><i></i>Harlow Ridge</div>
  <nav class="abs nav">
    <span class="active">Home</span><span>About Us</span><span>Services</span><span>Blog</span><span>Latest News</span><span>Contact</span>
  </nav>
</header>

<section class="abs hero" role="img" aria-label="Photo of a smiling sales team gathered around a meeting table">
  <h1>HARLOW RIDGE</h1>
  <p>RESULTS BUILT INTO EVERY REP</p>
  <div class="dots"><b></b><b></b><b></b><b></b></div>
</section>

<section class="welcome">
  <h2 class="abs section-title" style="left:0;top:726px">WELCOME TO OUR WEBSITE</h2>
  <p class="abs">Lorem ipsum dolor sit amet, consectetur adipiscing elit. Mauris placerat egestas egestas. Nunc ullamcorper iaculis iaculis. Vestibulum blandit urna vel enim imperdiet faucibus. Proin viverra ex magna, vitae aliquam purus laoreet quis. Donec pulvinar malesuada gravida. In hac habitasse platea dictumst. Maecenas non lectus vel diam fringilla imperdiet nec quis lorem. Integer hendrerit lorem cursus sapien dignissim, et condimentum libero scelerisque.<br>Cras condimentum diam justo, eu convallis lorem accumsan ut.</p>
  <span class="abs btn" style="left:507px;top:918px">Read More</span>
</section>

<section class="feature">
  <div class="abs photo-training" style="left:0;top:1041px;width:600px;height:401px" role="img" aria-label="Photo of a trainer presenting at a flip chart to a seated team"></div>
  <div class="abs panel" style="left:600px;top:1041px;width:600px;height:401px;padding:54px 0 0 45px">
    <svg width="60" height="44" viewBox="0 0 60 44"><g fill="var(--blue)"><rect x="6" y="24" width="7" height="16"/><rect x="17" y="14" width="7" height="26"/><rect x="28" y="20" width="7" height="20"/><rect x="39" y="6" width="7" height="34"/><rect x="0" y="40" width="58" height="3"/><rect x="0" y="0" width="3" height="43"/></g></svg>
    <h2>SALES TRAINING</h2>
    <p>Aliquam molestie, mi et imperdiet euismod, dui purus auctor tellus, et interdum lacus lectus et ante. Sed accumsan sollicitudin sapien, sit amet adipiscing turpis gravida ac.</p>
    <span class="btn">Read More</span>
  </div>
  <div class="abs" style="left:0;top:1442px;width:600px;height:401px;padding:60px 0 0 75px">
    <svg width="56" height="44" viewBox="0 0 56 44"><g fill="var(--blue)"><ellipse cx="22" cy="16" rx="22" ry="15"/><path d="M8 26l-4 12 14-8z"/><ellipse cx="38" cy="26" rx="16" ry="11" opacity=".85"/><path d="M46 34l6 9-12-6z" opacity=".85"/></g></svg>
    <h2>CONSULTING SERVICE</h2>
    <p>Aliquam molestie, mi et imperdiet euismod, dui purus auctor tellus, et interdum lacus lectus et ante. Sed accumsan sollicitudin sapien, sit amet adipiscing turpis gravida ac.</p>
    <span class="btn">Read More</span>
  </div>
  <div class="abs photo-consult" style="left:600px;top:1442px;width:600px;height:401px" role="img" aria-label="Photo of a consultant talking with a client at a desk"></div>
</section>

<section class="abs team">
  <h2 class="abs section-title" style="left:0;top:56px">OUR TEAM</h2>
  <svg class="abs" style="left:34px;top:222px" width="22" height="44" viewBox="0 0 22 44"><path d="M20 2L3 22l17 20" fill="none" stroke="#999" stroke-width="2"/></svg>
  <svg class="abs" style="left:1144px;top:222px" width="22" height="44" viewBox="0 0 22 44"><path d="M2 2l17 20L2 42" fill="none" stroke="#999" stroke-width="2"/></svg>
  <div class="abs member" style="left:61px;top:124px"><div class="avatar" role="img" aria-label="Portrait of a team member in a suit"></div><h3>NAME HEADING</h3><div class="role">Managing Director</div><p>Nulla vulputate nibh et felis euismod,<br>in tempus nisi iaculis...</p><div class="social"><i></i><i></i><i></i></div></div>
  <div class="abs member" style="left:331px;top:124px"><div class="avatar" role="img" aria-label="Portrait of a team member in a suit"></div><h3>NAME HEADING</h3><div class="role">Managing Director</div><p>Nulla vulputate nibh et felis euismod,<br>in tempus nisi iaculis...</p><div class="social"><i></i><i></i><i></i></div></div>
  <div class="abs member" style="left:601px;top:124px"><div class="avatar" role="img" aria-label="Portrait of a team member in a suit"></div><h3>NAME HEADING</h3><div class="role">Managing Director</div><p>Nulla vulputate nibh et felis euismod,<br>in tempus nisi iaculis...</p><div class="social"><i></i><i></i><i></i></div></div>
  <div class="abs member" style="left:871px;top:124px"><div class="avatar" role="img" aria-label="Portrait of a team member in a suit"></div><h3>NAME HEADING</h3><div class="role">Managing Director</div><p>Nulla vulputate nibh et felis euismod,<br>in tempus nisi iaculis...</p><div class="social"><i></i><i></i><i></i></div></div>
</section>

<section class="news">
  <h2 class="abs section-title" style="left:0;top:2380px">LATEST NEWS</h2>
  <article class="abs card" style="left:76px"><div class="photo news1" role="img" aria-label="Photo of a team meeting around a presentation board"></div><h3>Morbi dapibus ipsum</h3><p>Vivamus aliquet nulla tellus, tempus blandit massa pretium et. Quisque pretium nibh at vulputate dapibus...</p><time>Oct 23, 2018</time></article>
  <article class="abs card" style="left:436px"><div class="photo news2" role="img" aria-label="Photo of a colleague working at a computer"></div><h3>Morbi dapibus ipsum</h3><p>Vivamus aliquet nulla tellus, tempus blandit massa pretium et. Quisque pretium nibh at vulputate dapibus...</p><time>Oct 23, 2018</time></article>
  <article class="abs card" style="left:796px"><div class="photo news3" role="img" aria-label="Photo of business people reviewing documents"></div><h3>Morbi dapibus ipsum</h3><p>Vivamus aliquet nulla tellus, tempus blandit massa pretium et. Quisque pretium nibh at vulputate dapibus...</p><time>Oct 23, 2018</time></article>
</section>

<footer class="abs footer">
  <div class="abs" style="left:76px;top:46px;width:200px">
    <div style="display:flex;align-items:center;gap:8px;color:var(--white);font-weight:900;font-size:15px;text-transform:uppercase"><i style="width:20px;height:20px;border-radius:50%;background:var(--blue);display:block"></i>Harlow Ridge</div>
    <p style="margin-top:32px;line-height:20px;font-size:12px">Copyright © 2018. Harlow Ridge<br>All Right Reserved</p>
    <div class="fsocial"><i></i><i></i><i></i><i></i><i></i><i></i></div>
  </div>
  <div class="abs" style="left:343px;top:44px">
    <h4>Site Map</h4>
    <div style="display:flex;gap:54px"><ul><li>Home</li><li>About Us</li><li>Services</li><li>Blog</li></ul><ul><li>Latest News</li><li>Contact</li></ul></div>
  </div>
  <div class="abs contact" style="left:615px;top:44px">
    <h4>Contact Info</h4>
    <ul>
      <li style="color:var(--blue);font-weight:700;text-transform:uppercase;margin-bottom:6px">Harlow Ridge</li>
      <li><svg width="10" height="14" viewBox="0 0 10 14"><path fill="#aaa" d="M5 0a5 5 0 015 5c0 4-5 9-5 9S0 9 0 5a5 5 0 015-5z"/></svg><span>48 Cedar Hollow Road,<br>Brookfield NV 89300</span></li>
      <li><svg width="12" height="12" viewBox="0 0 24 24"><path fill="#aaa" d="M6.6 10.8a15 15 0 006.6 6.6l2.2-2.2c.3-.3.7-.4 1-.2 1.1.4 2.3.6 3.6.6.6 0 1 .4 1 1V20c0 .6-.4 1-1 1A17 17 0 013 4c0-.6.4-1 1-1h3.5c.6 0 1 .4 1 1 0 1.3.2 2.5.6 3.6.1.3 0 .7-.2 1z"/></svg><span>1-800-555-0142</span></li>
      <li><svg width="13" height="10" viewBox="0 0 24 18"><path fill="#aaa" d="M0 0h24v2L12 10 0 2zM0 4l12 8 12-8v14H0z"/></svg><span>hello@harlowridge.example</span></li>
    </ul>
  </div>
  <div class="abs" style="left:886px;top:44px">
    <h4>Email Sign Up</h4>
    <div class="email-input">Enter Email Address</div>
    <div class="signup">SIGN UP</div>
  </div>
</footer>

</body>
</html>
```